kleines Übersetzungsbüro sucht Design für Folder
Zielgruppe
Als Selbständige betreibe ich ein Italienisch-Übersetzungsbüro, das mit qualitativ hochwertigen Übersetzungen und maßgeschneidertem Service wirbt. Meine Tätigkeiten drehen sich um die Fachbereiche Recht und PR/Marketing/Corporate Communication.
Aufgabenstellung
Die Broschüre soll dynamisch,frisch, luftig, aber professionell wirken und gerne an den Stil meiner Website angelehnt sein.
Eine leicht minimalistische Gestaltung mit farbigen Akzenten (z.B. grafische Elemente) ist durchaus willkommen, aber nicht zwingend. Wenn das Endergebnis stimmig und überzeugend ist, lasse ich mich gerne umstimmen.
Auf das genaue Format des Folders möchte ich mich nicht festlegen. Ob einfach gefalzt, mit Wickel- oder Z-Falz: die Wahl überlasse ich Ihnen.
Der Folder soll zunächst nur per Mail übermittelt bzw. online verfügbar sein. Es empfiehlt sich also ein Format, bei dem die Inhalte überschaubar dargestellt sind und auf einen Blick erfasst werden können.
Alle CI-Farben sollten bei der Gestaltung berücksichtigt werden.
Vorgaben für die Verwendung vom Bildmaterial siehe hochgeladenes Briefingdokument.
Die Broschüre soll die Botschaft vermitteln, dass es sich lohnt auf einen dynamischen, zuverlässigen Profi zu setzen, der für einen immer da ist und pfiffige Leistungen erbringt.

```html
<!DOCTYPE html>
<html lang="de">
<head>
<meta charset="utf-8">
<title>Studio Ventresca – Folder</title>
<link rel="stylesheet" href="https://fonts.googleapis.com/css2?family=Alegreya+Sans:wght@400;500&display=swap">
<style>
  :root{
    --bg-top:#050505;
    --bg-bottom:#5c5c5c;
    --paper:#ffffff;
    --green:#7dc21e;
    --lime:#b9dc12;
    --ink:#4a4a4a;
  }
  *{box-sizing:border-box;margin:0;padding:0}
  html,body{width:1200px;height:848px;overflow:hidden}
  body{
    background:linear-gradient(180deg,var(--bg-top) 0%,var(--bg-top) 42%,var(--bg-bottom) 100%);
    font-family:"Alegreya Sans",sans-serif;color:var(--ink);
    position:relative;
  }
  .spread{
    position:absolute;top:163px;width:560px;height:522px;background:var(--paper);
    box-shadow:0 18px 28px rgba(0,0,0,.45);overflow:hidden;
  }
  .spread--front{left:25px}
  .spread--back{left:615px}
  .spread__art{position:absolute;inset:0;width:560px;height:522px}
  .panel{position:absolute;top:0;width:186.67px;height:522px}
  .panel--1{left:0}
  .panel--2{left:186.67px;background:linear-gradient(90deg,rgba(0,0,0,.06),rgba(0,0,0,0) 18%,rgba(0,0,0,0) 82%,rgba(0,0,0,.06))}
  .panel--3{left:373.33px}
  .block{position:absolute;left:18px;right:14px}
  .heading{color:var(--green);font-weight:500;font-size:12px;line-height:1.05;margin-bottom:6px}
  .heading--lg{font-size:15px}
  .body{font-size:5.4px;line-height:1.38;margin-bottom:5px}
  .list{font-size:5.4px;line-height:1.38;list-style:none;margin-bottom:5px}
  .brand{position:absolute;left:0;right:0;text-align:center}
  .brand__name{color:var(--green);font-size:17px;font-weight:500;letter-spacing:.02em}
  .brand__claim{color:var(--green);font-size:12px;line-height:1.15;margin-top:10px}
  .contact{font-size:5.6px;line-height:1.4;margin-top:12px}
  .signature{font-size:5.4px;line-height:1.38}
</style>
</head>
<body>

<!-- Außenseite: Seite 4, Seite 5, Titel -->
<section class="spread spread--front">
  <svg class="spread__art" viewBox="0 0 560 522" xmlns="http://www.w3.org/2000/svg">
    <defs>
      <linearGradient id="officeTone" x1="0" y1="0" x2="1" y2="1">
        <stop offset="0" stop-color="#e9eef3"/><stop offset="1" stop-color="#8ea4be"/>
      </linearGradient>
      <clipPath id="coverPanel"><rect x="373.33" y="0" width="186.67" height="522"/></clipPath>
      <clipPath id="page4Panel"><rect x="0" y="0" width="186.67" height="522"/></clipPath>
    </defs>
    <g clip-path="url(#page4Panel)">
      <ellipse cx="70" cy="228" rx="110" ry="74" transform="rotate(-8 70 228)" fill="none" stroke="var(--green)" stroke-width="12"/>
      <ellipse role="img" aria-label="Foto: Präsentation vor einem Bildschirm im Büro" cx="70" cy="228" rx="103" ry="67" transform="rotate(-8 70 228)" fill="url(#officeTone)"/>
    </g>
    <g clip-path="url(#coverPanel)">
      <path d="M395 0 Q500 15 560 70 L560 0 Z" fill="var(--lime)"/>
      <ellipse cx="505" cy="150" rx="112" ry="140" transform="rotate(-22 505 150)" fill="none" stroke="var(--green)" stroke-width="14"/>
      <ellipse role="img" aria-label="Foto: Handschlag in einem hellen Besprechungsraum" cx="505" cy="150" rx="103" ry="131" transform="rotate(-22 505 150)" fill="url(#officeTone)"/>
    </g>
    <path d="M0 478 Q280 548 560 478" fill="none" stroke="var(--lime)" stroke-width="10"/>
    <path d="M0 490 Q280 560 560 490 L560 522 L0 522 Z" fill="var(--paper)"/>
  </svg>

  <div class="panel panel--1">
    <div class="block" style="top:20px">
      <h2 class="heading">Ihre Investition<br>in Qualität</h2>
      <p class="body">Aufgrund ihres hohen Verwaltungsaufwands verlangen große Agenturen ein recht hohes Honorar. Der Übersetzer selbst erhält davon oft nur einen kleinen Teil. Wer direkt beauftragt, zahlt einen angemessenen Preis für die eigentliche Arbeit. Echte Qualität ist zu Dumpingpreisen nicht zu haben. Investieren Sie daher lieber direkt in das Endprodukt eines Profis.</p>
    </div>
    <div class="block" style="top:330px">
      <h2 class="heading">Meine Werte –<br>Ihr Mehrwert</h2>
      <p class="body">Meine Werte sind Ihr garantierter Mehrwert. Keine Umwege über ein Vermittlungsbüro: Ihr Auftrag landet direkt bei mir. Ich bin Ihre persönliche Ansprechpartnerin, auch dann, wenn andere Büros längst geschlossen haben. Kurze Wege, schnelle Antworten per E-Mail oder Telefon und echte Verlässlichkeit machen den Unterschied, Diskretion und Sorgfalt inklusive.</p>
    </div>
  </div>

  <div class="panel panel--2">
    <div class="block" style="top:20px">
      <h2 class="heading">Einige Highlights aus<br>meinem Portfolio</h2>
      <p class="body">Speziell für juristische Texte wie Verträge, AGB, Klagen, Urteile, Urkunden, Protokolle, Registerauszüge und Satzungen:</p>
      <ul class="list">
        <li>- Übersetzungen</li><li>- Beglaubigungen</li><li>- Einholung von Apostillen</li><li>- 4- und 6-Augenkontrolle</li><li>- Express-Service</li>
      </ul>
      <p class="body">Speziell für PR- und Marketingtexte wie Pressemitteilungen, Websites, Newsletter, Kundenmagazine, Unternehmensberichte, Kampagnen, Marktanalysen und Social Networks:</p>
      <ul class="list">
        <li>- Übersetzung, Adaptation und Transkreation</li><li>- Briefing im Vorfeld der Projektumsetzung</li><li>- Erstellung kundenspezifischer Glossare</li><li>- 4- und 6-Augenkontrolle</li><li>- Gut-zum-Druck</li>
      </ul>
    </div>
    <div class="block" style="top:299px">
      <h2 class="heading">Ihr direkter Draht zum<br>Übersetzungsprofi</h2>
      <p class="body">Wenn Sie eine Agentur beauftragen, haben Sie zwar einen Ansprechpartner, doch dieser übersetzt Ihren Text meist nicht selbst. Bei mir sprechen Sie direkt mit der Person, die Ihren Auftrag bearbeitet. Ich kenne Ihre Wünsche, kläre Rückfragen sofort und begleite jede Phase Ihres Projekts persönlich. So entsteht eine Zusammenarbeit, die nicht nur persönlicher, sondern auch effizienter ist – genau das, was Sie benötigen.</p>
    </div>
  </div>

  <div class="panel panel--3">
    <div class="brand" style="top:318px">
      <div class="brand__name">Studio Ventresca</div>
      <p class="brand__claim">Übersetzungen ins Italienische<br>präzise, persönlich, pfiffig</p>
      <p class="contact">Studio Ventresca<br>Inh.: Carla Ventresca<br>Lindenweg 7<br>66121 Musterstadt<br>Tel.: 0681 5550142<br>Mobil: 0152 5550198<br>Web: www.studio-ventresca.example<br>Mail: info@studio-ventresca.example</p>
    </div>
  </div>
</section>

<!-- Innenseite: Seite 1, Seite 2, Seite 3 -->
<section class="spread spread--back">
  <svg class="spread__art" viewBox="0 0 560 522" xmlns="http://www.w3.org/2000/svg">
    <defs>
      <linearGradient id="deskTone" x1="0" y1="0" x2="1" y2="0">
        <stop offset="0" stop-color="#9fb86a"/><stop offset=".35" stop-color="#f2f2f0"/><stop offset="1" stop-color="#dfe3e6"/>
      </linearGradient>
      <linearGradient id="officeTone2" x1="0" y1="0" x2="1" y2="1">
        <stop offset="0" stop-color="#e9eef3"/><stop offset="1" stop-color="#8ea4be"/>
      </linearGradient>
      <linearGradient id="portraitTone" x1="0" y1="0" x2="0" y2="1">
        <stop offset="0" stop-color="#efe7e2"/><stop offset="1" stop-color="#5aa64a"/>
      </linearGradient>
      <clipPath id="page3Panel"><rect x="373.33" y="0" width="186.67" height="522"/></clipPath>
      <clipPath id="page2Panel"><rect x="186.67" y="0" width="186.67" height="522"/></clipPath>
    </defs>
    <rect role="img" aria-label="Foto: Schreibtisch von oben mit Pflanze, Notizblock, Kaffeetasse und Tastatur" x="0" y="0" width="373.33" height="100" fill="url(#deskTone)"/>
    <g clip-path="url(#page3Panel)">
      <ellipse cx="480" cy="75" rx="108" ry="74" transform="rotate(-15 480 75)" fill="none" stroke="var(--green)" stroke-width="12"/>
      <ellipse role="img" aria-label="Foto: Geschäftsleute im Büro mit Diagrammen" cx="480" cy="75" rx="101" ry="67" transform="rotate(-15 480 75)" fill="url(#officeTone2)"/>
    </g>
    <g clip-path="url(#page2Panel)">
      <ellipse cx="300" cy="448" rx="98" ry="78" transform="rotate(-20 300 448)" fill="none" stroke="var(--green)" stroke-width="16"/>
      <ellipse role="img" aria-label="Porträtfoto der Übersetzerin" cx="300" cy="448" rx="88" ry="68" transform="rotate(-20 300 448)" fill="url(#portraitTone)"/>
    </g>
    <path d="M0 438 Q120 520 373 478 Q470 462 560 440" fill="none" stroke="var(--lime)" stroke-width="10"/>
  </svg>

  <div class="panel panel--1">
    <div class="block" style="top:112px">
      <h2 class="heading heading--lg">Wenn Großes im<br>Kleinen entsteht</h2>
      <p class="body">Qualität war schon immer eine Frage des Könnens – das gilt besonders für Übersetzungen. Deshalb überzeugt mein Büro seit über 13 Jahren private Kunden, Behörden und Unternehmen aller Größen mit einem hochwertigen Service, der keine Wünsche offen lässt. Frei nach dem Motto „Klein, aber fein“.</p>
      <p class="body">Vielleicht kann ich bald auch Sie überzeugen. Unterhalten Sie Geschäftsbeziehungen nach Italien? Planen Sie Marketing-Aktivitäten oder PR-Kampagnen für Ihre Zielgruppe im italienischen Sprachraum? Dann bin ich</p>
      <h2 class="heading" style="font-size:12.5px;margin-top:4px">Ihre Ansprechpartnerin<br>und Wegbegleiterin für<br>Italienisch-<br>Fachübersetzungen.</h2>
      <p class="signature">Carla Ventresca<br>Dottoressa in Traduzione<br>Italienisch-Deutsch-Englisch<br>Allg. beeid. Übersetzerin und Dolmetscherin<br>Mitglied im Fachverband Sprache e.V.<br>Übersetzerin<br>Korrektorin<br>Transkreative Texterin</p>
    </div>
  </div>

  <div class="panel panel--2">
    <div class="block" style="top:74px">
      <p class="body">Als italienische Muttersprachlerin verfüge ich über fundierte Sprachkenntnis und Feingefühl, die für Ihre Fachtexte unentbehrlich sind. Seit mehr als einem Jahrzehnt bin ich als selbständige Übersetzerin für hochwertige Fachtexte tätig. Meine akademische Ausbildung ergänze ich durch regelmäßige Weiterbildung in Fachwissen, Know-how und Sprachpflege.</p>
      <p class="body">Um eine qualitativ einwandfreie Leistung zu liefern, setze ich gängige CAT-Software ein. Doch Technik allein genügt nicht: Kompetenz, Kreativität und Feingefühl bringen erst die perfekte Übersetzung auf den Schreibtisch.</p>
      <p class="body">Juristische Übersetzungen und Übersetzungen im Bereich Marketing und PR – auf diese beiden Schwerpunkte habe ich mich spezialisiert. Erstere erfordern absolute Präzision, denn juristische Texte müssen eindeutig formuliert sein. Selbst kleinste Fehler können großen Schaden anrichten. Hier sollten Sie nichts dem Zufall überlassen.</p>
    </div>
  </div>

  <div class="panel panel--3">
    <div class="block" style="top:183px">
      <p class="body">Dank meiner einschlägigen Berufserfahrung verfüge ich über solide juristische Kenntnisse und garantiere Ihnen die strikte Einhaltung der Prinzipien der Rechtsübersetzung. Diskretion versteht sich von selbst. So sind Sie auf der sicheren Seite!</p>
      <p class="body">Übersetzungen für Marketing und Public Relations sind hingegen deutlich vielschichtiger. Es geht nicht um wortgetreue Übertragung, sondern darum, eine Zielgruppe mit anderem kulturellen Hintergrund zu erreichen und zu bewegen. Dazu brauchen Sie griffige, knackige und zielsprachlich authentische Texte einer Spezialistin für Adaptation und Transkreation. Mit meiner Sensibilität, textlichen Kreativität und meinem Repertoire an Schreibtechniken gelingt mir der Spagat zwischen Sprachen und Kulturen. Gemeinsam steigern wir die Attraktivität Ihres Images bei Ihrer Zielgruppe in Italien und im Tessin.</p>
    </div>
  </div>
</section>

</body>
</html>
```